A design led business card for the construction industry

High-end business card to match logo. White logo on dark grey/off black to the front. Matching dark font on white to back, possibly with logo design again.

We offer construction and project management services to commercial and private clients in the UK. Projetcs range from newbuilds, conversion of listed buildings and refurbishments and extensions of existing homes. Our focus is on quality and attention to detail using the highest skills.

Contact Information for Business Card

Name; Dorian Hatch BSc
Position; Project Manager
Mobile; 07962 804 157
Tel; 01632 958412
email; dorian@framelark.co.uk
web; www.framelark.co.uk
Address; Ashcombe on Vale, KT4 7PZ

Colors

Designer to choose only greyscale colors for use in the design.

Requirements
Must have
• To include the below description of the business,

CONSTRUCTION - PROJECT MANAGEMENT
Nice to have
• The posibility of the top back of the card being used as a ruler. So will have a measurement to scale in mm or an architect scale of 1:50
Should not have
• Should not be portrait

```html
<!DOCTYPE html>
<html lang="en">
<head>
<meta charset="utf-8">
<title>Framelark – Business Card</title>
<link rel="stylesheet" href="https://fonts.googleapis.com/css2?family=Roboto:wght@400;500;700&display=swap">
<style>
  :root {
    --backdrop: #e4e4e4;
    --card-dark: #1f1f1f;
    --card-light: #f4f4f4;
    --ink: #262626;
    --white: #ffffff;
  }
  * { margin: 0; padding: 0; box-sizing: border-box; }
  html, body {
    width: 1200px; height: 960px; overflow: hidden;
    background: var(--backdrop);
    font-family: "Roboto", Arial, sans-serif;
    color: var(--ink);
  }
  .card {
    position: absolute;
    left: 328px;
    width: 544px;
    height: 351px;
  }
  /* Front */
  .card-front {
    top: 110px;
    background: var(--card-dark);
  }
  .front-texture {
    position: absolute; inset: 0;
    background: linear-gradient(135deg, #4a4a4a 0%, #2a2a2a 35%, #1c1c1c 60%, #141414 100%);
  }
  .front-brand {
    position: absolute;
    left: 0; right: 0; top: 160px;
    text-align: center;
    color: var(--white);
    font-size: 22px;
    font-weight: 400;
    letter-spacing: 7px;
    padding-left: 7px;
  }
  /* Back */
  .card-back {
    top: 503px;
    background: var(--card-light);
  }
  .ruler { position: absolute; left: 0; top: 0; }
  .ruler-label { font-family: "Roboto", Arial, sans-serif; font-size: 9px; fill: var(--ink); }
  .brand-block {
    position: absolute;
    left: 30px; width: 224px;
    top: 155px;
    text-align: center;
    font-size: 19px;
    letter-spacing: 6px;
    padding-left: 6px;
    color: var(--ink);
  }
  .services {
    position: absolute;
    left: 30px; width: 224px;
    top: 276px;
    text-align: center;
    font-size: 15px;
    line-height: 18px;
    color: var(--ink);
  }
  .contact {
    position: absolute;
    left: 297px; top: 95px;
    font-size: 15px;
  }
  .contact-name { font-size: 19px; font-weight: 700; line-height: 24px; }
  .contact-role { line-height: 18px; }
  .contact-rule { width: 36px; height: 2px; background: var(--ink); margin: 32px 0 34px; }
  .contact-address { line-height: 18px; margin-bottom: 15px; }
  .contact-list { list-style: none; line-height: 18.7px; }
  .contact-list li { display: flex; align-items: center; }
  .contact-list svg { width: 13px; height: 13px; margin-right: 5px; flex: none; }
</style>
</head>
<body>

<section class="card card-front">
  <div class="front-texture" role="img" aria-label="Dark grey card face with a faint repeating brand texture fading from light grey at top left to near black"></div>
  <div class="front-brand">FRAMELARK</div>
</section>

<section class="card card-back">
  <svg class="ruler" width="544" height="40" viewBox="0 0 544 40" aria-label="1:50 architect scale ruler">
    <defs>
      <pattern id="minor-ticks" x="32" y="0" width="12.8" height="18" patternUnits="userSpaceOnUse">
        <rect x="0" y="0" width="1" height="18" fill="#262626"/>
      </pattern>
    </defs>
    <rect x="32" y="0" width="501" height="18" fill="url(#minor-ticks)"/>
    <g fill="#262626">
      <rect x="32" y="0" width="1" height="37"/>
      <rect x="160" y="0" width="1" height="37"/>
      <rect x="288" y="0" width="1" height="37"/>
      <rect x="416" y="0" width="1" height="37"/>
      <rect x="96" y="0" width="1" height="25"/>
      <rect x="224" y="0" width="1" height="25"/>
      <rect x="352" y="0" width="1" height="25"/>
      <rect x="480" y="0" width="1" height="25"/>
    </g>
    <text class="ruler-label" x="7" y="36">1:50</text>
    <text class="ruler-label" x="165" y="36">1m</text>
    <text class="ruler-label" x="293" y="36">2m</text>
    <text class="ruler-label" x="421" y="36">3m</text>
  </svg>

  <div class="brand-block">FRAMELARK</div>
  <p class="services">CONSTRUCTION<br>PROJECT MANAGEMENT</p>

  <div class="contact">
    <p class="contact-name">Dorian Hatch BSc</p>
    <p class="contact-role">Project Manager</p>
    <div class="contact-rule"></div>
    <p class="contact-address">Ashcombe on Vale, KT4 7PZ</p>
    <ul class="contact-list">
      <li><svg viewBox="0 0 13 13"><rect x="3.5" y="0.5" width="6" height="12" rx="1" fill="none" stroke="#262626"/><rect x="5.5" y="10" width="2" height="1" fill="#262626"/></svg>07962 804 157</li>
      <li><svg viewBox="0 0 13 13"><path d="M2.5 1 L5 1 L6 4 L4.5 5.2 C5.3 7 6 7.8 7.8 8.6 L9 7 L12 8 L12 10.5 C12 11.5 11 12 10 12 C5.5 11.5 1.5 7.5 1 3 C1 2 1.5 1 2.5 1 Z" fill="#262626"/></svg>01632 958412</li>
      <li><svg viewBox="0 0 13 13"><rect x="0.5" y="2.5" width="12" height="8" fill="none" stroke="#262626"/><path d="M0.5 2.5 L6.5 7 L12.5 2.5" fill="none" stroke="#262626"/></svg>dorian@framelark.co.uk</li>
      <li><svg viewBox="0 0 13 13"><circle cx="6.5" cy="6.5" r="5.8" fill="none" stroke="#262626"/><ellipse cx="6.5" cy="6.5" rx="2.6" ry="5.8" fill="none" stroke="#262626"/><path d="M0.7 6.5 H12.3 M1.6 3.5 H11.4 M1.6 9.5 H11.4" stroke="#262626"/></svg>www.framelark.co.uk</li>
    </ul>
  </div>
</section>

</body>
</html>
```